Fast-casual chicken restaurant Plume Rally needs a catering menu design

We need a catering menu designed for Plume Rally. We are looking to design a 24x36in landscape menu board for our new catering menu. The catering memo attached includes our catering menu and Plume Rally branding. More information about our brand can be found at https://plumerally.example/.

```html
<!DOCTYPE html>
<html lang="en">
<head>
<meta charset="utf-8">
<title>Plume Rally Catering Menu</title>
<link rel="stylesheet" href="https://fonts.googleapis.com/css2?family=Montserrat:wght@500;600&display=swap">
<style>
  :root {
    --red: #d63b2a;
    --yellow: #fccf2f;
    --white: #ffffff;
    --photo-a: #b8451f;
    --photo-b: #7a3b1c;
    --photo-c: #c98a3e;
  }
  * { box-sizing: border-box; margin: 0; padding: 0; }
  html, body { width: 1200px; height: 800px; overflow: hidden; }
  body { font-family: "Montserrat", sans-serif; font-weight: 500; }
  .menu-board { position: relative; width: 1200px; height: 800px; background: var(--white); overflow: hidden; }
  .backdrop { position: absolute; inset: 0; }
  .photo { position: absolute; top: 18px; height: 195px; }
  .photo-left { left: 19px; width: 575px; background: linear-gradient(120deg, var(--photo-c), var(--photo-a) 45%, var(--photo-b)); }
  .photo-right { left: 607px; width: 576px; background: linear-gradient(100deg, var(--photo-a), var(--photo-c) 40%, var(--photo-b) 75%, var(--photo-c)); }
  .section-title { position: absolute; font-weight: 600; font-size: 21.5px; letter-spacing: 0.3px; line-height: 1; transform: translate(-50%, -50%); white-space: nowrap; }
  .on-red { color: var(--yellow); }
  .on-white { color: var(--red); }
  .menu-table { position: absolute; border-collapse: collapse; table-layout: fixed; font-size: 11.3px; line-height: 15.3px; }
  .menu-table th { height: 30px; font-weight: 500; text-align: left; padding-left: 18px; vertical-align: middle; }
  .menu-table td { padding-left: 18px; vertical-align: top; white-space: nowrap; overflow: hidden; }
  .dark-table { background: var(--red); color: var(--white); border: 1px solid var(--yellow); }
  .dark-table th { background: var(--yellow); color: var(--red); }
  .dark-table td { border-left: 1px solid var(--yellow); border-top: 1px solid var(--yellow); }
  .light-table { background: var(--white); color: var(--red); border: 1px solid var(--red); }
  .light-table th { background: var(--red); color: var(--yellow); }
  .light-table td { border-left: 1px solid var(--red); border-top: 1px solid var(--red); }
  .center { text-align: center; padding-left: 0 !important; }
  .middle { vertical-align: middle !important; }
  .gap-top td { padding-top: 8px; }
  .gap-bottom td { padding-bottom: 7px; }
  .packaged { left: 27px; top: 272px; width: 577px; }
  .per-person { left: 28px; top: 443px; width: 577px; }
  .a-la-carte { left: 727px; top: 297px; width: 433px; }
  .catering { left: 347px; top: 644px; width: 813px; }
  .catering td { border-top: none; }
  .catering tr.ruled td { border-top: 1px solid var(--yellow); }
  .brand { position: absolute; left: 30px; top: 730px; display: flex; align-items: center; gap: 10px; }
  .brand-mark { width: 26px; height: 26px; border-radius: 50%; background: var(--red); }
  .brand-name { font-weight: 600; font-size: 30px; color: var(--red); letter-spacing: 0.5px; }
</style>
</head>
<body>
<main class="menu-board">
  <svg class="backdrop" width="1200" height="800" viewBox="0 0 1200 800" aria-hidden="true">
    <rect x="0" y="196" width="1200" height="604" fill="var(--red)"/>
    <path fill="var(--white)" d="M796 213 L1161 213 L1161 232 C1175 238 1190 236 1200 238 L1200 502 C1150 500 1090 505 1040 530 C960 565 900 600 880 618 C872 626 862 626 855 618 C830 590 815 545 780 515 C740 485 690 470 665 430 C620 370 628 300 690 258 C720 240 760 236 778 235 Z"/>
    <rect x="0" y="0" width="1200" height="196" fill="var(--white)"/>
    <path fill="var(--white)" d="M0 704 C40 680 90 660 140 663 C180 666 200 685 240 680 C300 675 320 720 316 800 L0 800 Z"/>
    <g fill="none" stroke="var(--yellow)" stroke-width="3">
      <polyline points="133,232 141,247 195,247"/><polyline points="437,247 492,247 500,232"/>
      <polyline points="111,401 119,416 174,416"/><polyline points="437,416 492,416 500,401"/>
      <polyline points="431,602 439,617 493,617"/><polyline points="756,617 811,617 819,602"/>
    </g>
    <g fill="none" stroke="var(--red)" stroke-width="3">
      <polyline points="796,257 804,272 859,272"/><polyline points="1026,272 1081,272 1089,257"/>
    </g>
  </svg>

  <div class="photo photo-left" role="img" aria-label="Photo of platters of sauced chicken wings, tenders, waffle fries, ribs and onion rings on a wooden table"></div>
  <div class="photo photo-right" role="img" aria-label="Photo of a large tray of mixed wings with ribs, onion rings and waffle fries"></div>

  <h2 class="section-title on-red" style="left:316px;top:247px">PACKEGED DEALS</h2>
  <table class="menu-table dark-table packaged">
    <colgroup><col style="width:101px"><col style="width:61px"><col style="width:331px"><col style="width:84px"></colgroup>
    <thead><tr><th>Name</th><th class="center">Feeds</th><th>Items</th><th>Price</th></tr></thead>
    <tbody>
      <tr class="gap-top"><td>Family</td><td class="center">4</td><td>12tenders, Sauces, Dressing, Large Side, 2L</td><td>$24.99</td></tr>
      <tr><td>Tailgate</td><td class="center">10</td><td>20tenders, 30 Wings, Sauces, Dressings, 1 Party Side</td><td>$75.99</td></tr>
      <tr class="gap-bottom"><td>House Party</td><td class="center">10</td><td>20tenders, 60 Wings, Sauces,<br>2 Party Sides, 2 Party Salads,&nbsp; Dressings, 2 2L</td><td>$155.99</td></tr>
    </tbody>
  </table>

  <h2 class="section-title on-red" style="left:305px;top:416px">PER PERSON DEALS</h2>
  <table class="menu-table dark-table per-person">
    <colgroup><col style="width:105px"><col style="width:62px"><col style="width:324px"><col style="width:86px"></colgroup>
    <thead><tr><th>Name</th><th class="center">Feeds</th><th style="padding-left:34px">Items</th><th>Price</th></tr></thead>
    <tbody>
      <tr class="gap-top"><td>Snack<br>(Par Person)</td><td class="center middle">1</td><td style="padding-left:34px">2tenders, Sauces, Dressing, 1 Reg Side</td><td class="middle">$7.00</td></tr>
      <tr><td>Party<br>(Par Person)</td><td class="center middle">1</td><td style="padding-left:34px">2 Tenders, 3 Wings, Sauces, Dressing, 1 Reg Side<br>12 OZ/fountain Drink</td><td class="middle">$11.00</td></tr>
      <tr class="gap-bottom"><td>Feast<br>(Par Person)</td><td class="center middle">1</td><td style="padding-left:34px">2 Tenders, 6 Wings, Sauces, Dressing, 1 Reg Side<br>Dessert, 20 OZ Drink</td><td class="middle">$15.00</td></tr>
    </tbody>
  </table>

  <h2 class="section-title on-white" style="left:941px;top:272px">A LA CARTE</h2>
  <table class="menu-table light-table a-la-carte">
    <colgroup><col style="width:195px"><col style="width:133px"><col style="width:105px"></colgroup>
    <thead><tr><th style="padding-left:30px">Items</th><th style="padding-left:29px">Increments</th><th style="padding-left:33px">Price</th></tr></thead>
    <tbody>
      <tr class="gap-top"><td style="padding-left:30px">Wings</td><td style="padding-left:29px">50,75,100</td><td style="padding-left:33px">$xx.xx</td></tr>
      <tr><td style="padding-left:30px">Tenders</td><td style="padding-left:29px">30,45,60</td><td style="padding-left:33px">$xx.xx</td></tr>
      <tr><td style="padding-left:30px">Waffle Fries</td><td style="padding-left:29px">Party Size</td><td style="padding-left:33px">$13.99</td></tr>
      <tr><td style="padding-left:30px">Grlic Parm Tots</td><td style="padding-left:29px">Party Size</td><td style="padding-left:33px">$13.99</td></tr>
      <tr><td style="padding-left:30px">Chicken Caesar Salad</td><td style="padding-left:29px">Party Size</td><td style="padding-left:33px">$38.99</td></tr>
      <tr><td style="padding-left:30px">Caesar Salad</td><td style="padding-left:29px">Party Size</td><td style="padding-left:33px">$27.99</td></tr>
      <tr><td style="padding-left:30px">Any Sauce</td><td style="padding-left:29px">8 OZ</td><td style="padding-left:33px">$1.99</td></tr>
      <tr class="gap-bottom"><td style="padding-left:30px">Cheese Sauce</td><td style="padding-left:29px">8 OZ</td><td style="padding-left:33px">$2.49</td></tr>
    </tbody>
  </table>

  <h2 class="section-title on-red" style="left:625px;top:617px">CATERING MENU</h2>
  <table class="menu-table dark-table catering">
    <colgroup><col style="width:153px"><col style="width:136px"><col style="width:202px"><col style="width:176px"><col style="width:146px"></colgroup>
    <thead><tr><th style="padding-left:22px">Flavors</th><th>BBQ</th><th>Dry Rubs</th><th>Teriyaki</th><th>Buffalo</th></tr></thead>
    <tbody>
      <tr class="gap-top"><td style="padding-left:22px">Honey Mustard</td><td>Cajun BBQ</td><td>7 Pepper</td><td>Cajun Teriyaki</td><td>Mellow</td></tr>
      <tr><td style="padding-left:22px">Hot Lemon Papper</td><td>Citrus Chipotle</td><td>Cajun</td><td>Spicy Teriyaki</td><td>Steady Simmer</td></tr>
      <tr class="ruled"><td style="padding-left:22px">Lamaican Jerk</td><td>Golden BBQ</td><td>Garlic Parm</td><td>Traditional Teriyaki</td><td>Red Ember</td></tr>
      <tr class="ruled"><td style="padding-left:22px">Mango Habanero</td><td>Honey BBQ</td><td>Lemon Pepper</td><td></td><td>Hot Coal</td></tr>
      <tr class="ruled gap-bottom"><td style="padding-left:22px">Sweet Chili</td><td>Kickin BBQ</td><td>West Texas Mesquite</td><td></td><td>Scorcher</td></tr>
    </tbody>
  </table>

  <div class="brand">
    <span class="brand-mark"></span>
    <span class="brand-name">Plume Rally</span>
  </div>
</main>
</body>
</html>
```